Harbor Crest Metrics Company Website Design and Coding

We want to redesign our existing website so that it is more visually and functionally appealing to prospective clients and potential job candidates. We would like to keep our current color scheme and implement our current logo as well. We have a high-level idea of website structure that we are thinking of, which is in the attached files. Logo is included as well. The final design would ideally be energy and analytics focused. We will need the new website to be coded as well, please.

Target Market(s)

Energy and utility industry

Industry/Entity Type

Energy/analytics

Coding

Coded - Design and coding required

Number of Pages Required

5+ page

Font styles to use
Sans Serif

Colors
0094D4
00A9DD
6FCCEA
C7EBF8
E9F6FB
F0912C
F2A743
F7CA91
FBE8D2
FDF5EE

Requirements
Must have
• Consistent color scheme- please use the one that we provided. We need an overview, a home page, and our core services. A separate job application page. Logo must be incorporated. We would like e "Meet our Team" page. Please include all of the content that is listed in our attachments.
Nice to have
• Movement
Should not have
• No music, no cartoons/animation, no pictures of a chalkboard

```html
<!DOCTYPE html>
<html lang="en">
<head>
<meta charset="utf-8">
<title>Harbor Crest Metrics</title>
<link href="https://fonts.googleapis.com/css2?family=Fira+Sans:wght@500;600;700&family=Roboto:wght@400;500;700&display=swap" rel="stylesheet">
<style>
:root{
  --blue:#1a7fd0;
  --blue-deep:#1570c2;
  --blue-bright:#2196e3;
  --sky:#6fccea;
  --ink:#111;
  --text:#444;
  --muted:#666;
  --orange:#e98222;
  --paper:#fff;
  --line:#d9d9d9;
}
*{box-sizing:border-box;margin:0;padding:0}
html,body{width:1200px;height:4914px;overflow:hidden}
body{position:relative;background:var(--paper);font-family:"Roboto",sans-serif;color:var(--text)}
.abs{position:absolute}
h1,h2,h3{font-family:"Fira Sans",sans-serif;color:var(--ink)}
.btn{position:absolute;display:flex;align-items:center;justify-content:center;gap:8px;border-radius:24px;font:700 13px "Roboto",sans-serif;text-transform:uppercase;letter-spacing:.2px}
.btn .arr{width:14px;height:14px;border-radius:50%;display:inline-flex;align-items:center;justify-content:center;font-size:9px}
.btn-light{border:2px solid #fff;color:#fff}
.btn-light .arr{background:#fff;color:var(--blue)}
.btn-blue{border:2px solid var(--blue);color:var(--blue)}
.btn-blue .arr{background:var(--blue);color:#fff}
.ph{position:absolute}

/* header */
.topline{left:0;top:0;width:1200px;height:4px;background:var(--blue)}
.brand{left:56px;top:40px;display:flex;align-items:center;gap:10px;font:500 19px "Roboto",sans-serif;color:var(--blue-deep)}
.brand .mark{width:26px;height:26px;border-radius:50%;background:var(--sky)}
.nav{left:508px;top:49px;display:flex;gap:26px;font:500 13.5px "Roboto",sans-serif;color:#222}
.nav .on{color:var(--blue)}
.login{left:977px;top:34px;width:110px;height:46px;border:2px solid var(--blue-deep);border-radius:24px;font:700 13.5px "Roboto",sans-serif;color:var(--blue-deep);display:flex;align-items:center;justify-content:center;gap:6px}

/* hero */
.hero{left:0;top:116px;width:1200px;height:804px;background:linear-gradient(100deg,#2e3640 0%,#4a5560 45%,#3b4652 100%)}
.hero-title{left:112px;top:282px;font:700 54px/68px "Fira Sans",sans-serif;color:#fff}
.dots{left:117px;top:672px;display:flex;gap:7px}
.dots i{width:11px;height:11px;border-radius:50%;border:2px solid #fff}
.dots i.on{background:#fff}

/* services */
.center{width:1200px;text-align:center;left:0}
.sec-title{font:700 46px "Fira Sans",sans-serif;color:var(--ink)}
.svc-ring{position:absolute;width:166px;height:166px;border-radius:50%;border:5px solid var(--blue);border-top-color:transparent;transform:rotate(-20deg)}
.svc-icon{position:absolute;width:90px;height:90px}
.svc-label{position:absolute;width:280px;text-align:center;font:500 20px/26px "Fira Sans",sans-serif;color:#222}

/* who */
.who-band{left:0;top:1540px;width:1200px;height:598px;background:var(--blue)}
.who-title{left:682px;top:1620px;font:700 46px "Fira Sans",sans-serif;color:#fff}
.who-text{left:682px;top:1706px;width:452px;font:13.5px/25.8px "Roboto",sans-serif;color:#fff;text-align:justify}

/* team */
.card{position:absolute;width:185px;height:234px;border:3px solid var(--blue-bright);border-radius:4px;background:#fff;text-align:center}
.card .cut{position:absolute;left:22px;right:22px;top:-4px;height:6px;background:#fff}
.avatar{position:absolute;width:118px;height:118px;border-radius:50%;background:linear-gradient(#b9c2cb,#6f7b86)}
.card .name{position:absolute;left:0;width:100%;top:108px;font:500 19px "Fira Sans",sans-serif;color:var(--blue-deep)}
.card .co{position:absolute;left:0;width:100%;top:140px;font:13px "Roboto",sans-serif;color:#333}
.card .soc{position:absolute;left:73px;top:172px;width:34px;height:34px;border-radius:50%;background:var(--blue-bright)}

/* careers */
.careers-band{left:0;top:2677px;width:1200px;height:521px;background:var(--orange)}
.careers-title{left:108px;top:2740px;font:700 46px "Fira Sans",sans-serif;color:#fff}
.careers-text{left:108px;top:2810px;width:455px;font:13.5px/25.8px "Roboto",sans-serif;color:#fff;text-align:justify}

/* case study */
.case-band{left:0;top:3198px;width:1200px;height:1330px;background:linear-gradient(180deg,#f1f1f3,#e6e6e8)}
.rule{left:570px;top:3356px;width:60px;height:3px;background:var(--ink)}
.case-title{font:500 40px/50px "Fira Sans",sans-serif;color:#111}
.case-text{width:490px;font:13.5px/25.8px "Roboto",sans-serif;color:#555;text-align:justify}

/* footer */
.f-head{font:700 18px "Roboto",sans-serif;color:#111;letter-spacing:.3px}
.f-bar{width:45px;height:3px;background:#111;margin-top:8px}
.f-list{list-style:none;margin-top:14px;font:14px/22px "Roboto",sans-serif;color:#444}
.f-list li::before{content:"»";margin-right:12px;color:#444}
.contact-row{display:flex;gap:12px;font:14px/22px "Roboto",sans-serif;color:#444}
.contact-row svg{flex:none;margin-top:4px}
.socials{left:155px;top:4692px;display:flex;gap:8px}
.socials i{width:25px;height:25px;border-radius:50%;background:var(--blue-deep)}
.socials i:nth-child(3),.socials i:nth-child(4){background:#d2344a}
.divider{left:110px;top:4832px;width:980px;height:1px;background:var(--line)}
.copy{left:0;top:4862px;width:1200px;text-align:center;font:13px "Roboto",sans-serif;color:#222}
</style>
</head>
<body>

<!-- header -->
<div class="abs topline"></div>
<div class="abs brand"><span class="mark"></span>Harbor Crest Metrics</div>
<nav class="abs nav"><span class="on">Home</span><span>About us</span><span>Services</span><span>Our Work</span><span>Blog</span><span>Contact us</span></nav>
<div class="abs login">
  <svg width="12" height="13" viewBox="0 0 12 13"><circle cx="6" cy="3.5" r="3" fill="currentColor"/><path d="M0 13c0-4 2.5-6 6-6s6 2 6 6z" fill="currentColor"/></svg>Login
</div>

<!-- hero -->
<div class="ph hero" role="img" aria-label="Photo of an analyst working at a laptop with data overlay graphics"></div>
<h1 class="abs hero-title">Customer<br>Segmentation<br>and Targeting</h1>
<div class="btn btn-light" style="left:112px;top:506px;width:162px;height:42px">Get Started <span class="arr">&#10148;</span></div>
<div class="abs dots"><i></i><i class="on"></i><i></i><i></i></div>
<svg class="abs" style="left:0;top:580px" width="1200" height="345" viewBox="0 0 1200 345">
  <path d="M0 345 L0 330 C150 250 420 210 700 200 C950 190 1130 175 1200 110 L1200 345 Z" fill="#fff"/>
  <path d="M0 335 C150 250 420 200 700 192 C950 186 1140 180 1200 95 L1200 150 C1140 185 950 200 700 205 C420 215 150 262 0 345 Z" fill="var(--blue)"/>
</svg>

<!-- what we do -->
<h2 class="abs center sec-title" style="top:856px">What We Do</h2>
<p class="abs center" style="top:934px;font-size:13px;color:#444">Al A Cart Services - All in one integrated ecosystem. Built for either your staff or ours to get results.</p>

<div class="svc-ring" style="left:149px;top:990px"></div>
<svg class="svc-icon" style="left:187px;top:1028px" viewBox="0 0 90 90" fill="none" stroke="var(--blue)" stroke-width="2.5"><circle cx="38" cy="42" r="18"/><path d="M51 55l16 16"/><rect x="60" y="62" width="22" height="18" stroke="var(--orange)"/><path d="M30 48v-8M38 48V36M46 48v-5"/></svg>
<div class="svc-label" style="left:92px;top:1168px">Predictive Analytics and Forecasting</div>

<div class="svc-ring" style="left:425px;top:990px"></div>
<svg class="svc-icon" style="left:463px;top:1028px" viewBox="0 0 90 90" fill="none" stroke="var(--blue)" stroke-width="2.5"><rect x="18" y="12" width="44" height="64" rx="4"/><rect x="25" y="19" width="30" height="12"/><path d="M25 40h8M37 40h8M25 50h8M37 50h8M25 60h8M37 60h8"/><circle cx="64" cy="62" r="12" stroke="var(--orange)"/><path d="M64 55v14" stroke="var(--orange)"/></svg>
<div class="svc-label" style="left:368px;top:1168px">T&amp;D Planning</div>

<div class="svc-ring" style="left:637px;top:990px"></div>
<svg class="svc-icon" style="left:675px;top:1028px" viewBox="0 0 90 90" fill="none" stroke="var(--blue)" stroke-width="2.5"><path d="M24 14h34l12 12v52H24z"/><path d="M32 40h30M32 50h30M32 60h30M32 70h20"/><path d="M18 12l10 8-6 6z" stroke="var(--orange)"/></svg>
<div class="svc-label" style="left:580px;top:1168px">Evaluation</div>

<div class="svc-ring" style="left:914px;top:990px"></div>
<svg class="svc-icon" style="left:952px;top:1028px" viewBox="0 0 90 90" fill="none" stroke="var(--blue)" stroke-width="2.5"><rect x="30" y="14" width="42" height="56"/><path d="M38 52V40M46 52V32M54 52V44M62 52V28"/><rect x="16" y="44" width="26" height="30" rx="3"/><circle cx="29" cy="59" r="6" stroke="var(--orange)"/></svg>
<div class="svc-label" style="left:857px;top:1168px">Pilot &amp; Emerging Tech Support</div>

<div class="svc-ring" style="left:272px;top:1227px"></div>
<svg class="svc-icon" style="left:310px;top:1265px" viewBox="0 0 90 90" fill="none" stroke="var(--blue)" stroke-width="2.5"><circle cx="45" cy="34" r="22"/><path d="M37 28l-6 6 6 6M53 28l6 6-6 6M48 24l-6 20" stroke="var(--orange)"/><rect x="22" y="58" width="46" height="16" rx="2"/><path d="M14 78h62"/></svg>
<div class="svc-label" style="left:215px;top:1405px">Program Portfolio &amp; Resource Planning</div>

<div class="svc-ring" style="left:792px;top:1227px"></div>
<svg class="svc-icon" style="left:830px;top:1265px" viewBox="0 0 90 90" fill="none" stroke="var(--blue)" stroke-width="2.5"><circle cx="28" cy="30" r="6"/><circle cx="45" cy="30" r="6"/><circle cx="62" cy="30" r="6"/><path d="M18 50c0-8 20-8 20 0M35 50c0-8 20-8 20 0M52 50c0-8 20-8 20 0"/><path d="M12 66c14-6 26 4 40 0l20-8"/><path d="M28 16l2 4 4 0-3 3 1 4-4-2-4 2 1-4-3-3 4 0z" stroke="var(--orange)"/></svg>
<div class="svc-label" style="left:735px;top:1405px">Program Delivery Support</div>

<!-- who we are -->
<div class="abs who-band"></div>
<svg class="abs" style="left:0;top:1540px" width="640" height="598" viewBox="0 0 640 598">
  <path d="M560 0 C650 170 630 450 510 598 L430 598 C540 450 560 200 470 0 Z" fill="var(--blue-bright)"/>
</svg>
<div class="ph" style="left:0;top:1540px;width:560px;height:598px;background:linear-gradient(120deg,#b79a7c,#d8cfc3 55%,#8a7d70);clip-path:path('M0 0 H470 C560 200 540 450 430 598 H0 Z')" role="img" aria-label="Photo of a team collaborating around a laptop in an office"></div>
<h2 class="abs who-title">Who We Are</h2>
<p class="abs who-text">Harbor Crest Metrics (HCM) was formed in 2016 to help utilities and regulatory agencies navigate the technical, economic, and policy challenges of building a smarter and cleaner energy future. Our research focuses on impact analysis as well as predictive and causal analytics. We deliver data-driven insights into how various technologies and interventions affect the way homes and businesses use energy and how those in turn affect grid and system planning. We have a proven record for conducting high-quality, accurate, and unbiased analysis and are meticulous about ensuring that research is useful for policy decisions, operations, and implementation.</p>
<div class="btn btn-light" style="left:681px;top:1995px;width:186px;height:44px">More About Us <span class="arr">&#10148;</span></div>

<!-- team -->
<h2 class="abs center sec-title" style="top:2212px">Our Team</h2>
<div class="card" style="left:110px;top:2342px"><div class="cut"></div><div class="name">John Doe</div><div class="co">Company name</div><div class="soc"></div></div>
<div class="card" style="left:375px;top:2342px"><div class="cut"></div><div class="name">John Doe</div><div class="co">Company name</div><div class="soc"></div></div>
<div class="card" style="left:641px;top:2342px"><div class="cut"></div><div class="name">John Doe</div><div class="co">Company name</div><div class="soc"></div></div>
<div class="card" style="left:906px;top:2342px"><div class="cut"></div><div class="name">John Doe</div><div class="co">Company name</div><div class="soc"></div></div>
<div class="avatar" style="left:141px;top:2318px" role="img" aria-label="Team member portrait"></div>
<div class="avatar" style="left:406px;top:2318px" role="img" aria-label="Team member portrait"></div>
<div class="avatar" style="left:672px;top:2318px;background:linear-gradient(#8fcbe8,#4a7fa6)" role="img" aria-label="Team member portrait"></div>
<div class="avatar" style="left:937px;top:2318px" role="img" aria-label="Team member portrait"></div>

<!-- careers -->
<div class="abs careers-band"></div>
<h2 class="abs careers-title">Careers</h2>
<p class="abs careers-text">At HCM, we are driven to help create a smarter and cleaner energy future, and we are always looking for talented professionals who share our passion for achieving this goal. We are a transparent organization where you will have the opportunity to work directly with our senior energy experts. Our employees get to work on a wide variety of projects and develop new skills so that they are well equipped to interact with our clients find effective ways to solve our clients' problems. The work is not easy, but the rewards of working with senior experts and the opportunities for growth will be worth it.</p>
<div class="btn btn-light" style="left:107px;top:3064px;width:188px;height:44px">More About Us <span class="arr">&#10148;</span></div>
<div class="ph" style="left:600px;top:2758px;width:490px;height:340px;border-radius:40px;background:linear-gradient(110deg,#e9e6e1,#b8c4cf 60%,#f2f0ec)" role="img" aria-label="Photo of a smiling professional working on a laptop"></div>

<!-- case study -->
<div class="abs case-band"></div>
<h2 class="abs center sec-title" style="top:3294px">Case Study</h2>
<div class="abs rule"></div>

<h3 class="abs case-title" style="left:130px;top:3450px">Journal Articles and<br>Conference Presentations</h3>
<p class="abs case-text" style="left:130px;top:3556px">Lorem ipsum dolor sit amet, consectetur adipiscing elit, sed do eiusmod tempor incididunt ut labore et dolore magna aliqua. Ut enim ad minim veniam, quis nostrud exercitation ullamco laboris nisi ut aliquip ex ea commodo consequat. Duis aute irure dolor in reprehenderit in voluptate velit esse cillum dolore eu fugiat nulla pariatur. Excepteur sint occaecat cupidatat culpa qui officia deserunt mollit anim id est laborum.</p>
<div class="btn btn-blue" style="left:130px;top:3736px;width:188px;height:44px">Learn More <span class="arr">&#10148;</span></div>
<svg class="abs" style="left:640px;top:3390px" width="460" height="430" viewBox="0 0 460 430"><circle cx="230" cy="215" r="208" fill="none" stroke="var(--blue)" stroke-width="9" stroke-dasharray="0 430 560 400" transform="rotate(-30 230 215)"/></svg>
<div class="ph" style="left:660px;top:3400px;width:410px;height:410px;border-radius:50%;background:radial-gradient(circle at 55% 55%,#23344d,#6b7480 70%,#c9c2b5)" role="img" aria-label="Photo of a laptop displaying analytics dashboards"></div>

<svg class="abs" style="left:100px;top:3850px" width="450" height="450" viewBox="0 0 450 450"><circle cx="225" cy="225" r="216" fill="none" stroke="var(--blue)" stroke-width="9" stroke-dasharray="0 700 520 200" transform="rotate(10 225 225)"/></svg>
<div class="ph" style="left:118px;top:3868px;width:414px;height:414px;border-radius:50%;background:radial-gradient(circle at 50% 40%,#c6b7b2,#4d4e78 60%,#272a4a)" role="img" aria-label="Photo of a meeting reviewing charts on a large screen"></div>
<h3 class="abs case-title" style="left:578px;top:3950px">Published Reports</h3>
<p class="abs case-text" style="left:580px;top:4016px">Lorem ipsum dolor sit amet, consectetur adipiscing elit, sed do eiusmod tempor incididunt ut labore et dolore magna aliqua. Ut enim ad minim veniam, quis nostrud exercitation ullamco laboris nisi ut aliquip ex ea commodo consequat. Duis aute irure dolor in reprehenderit in voluptate velit esse cillum dolore eu fugiat nulla pariatur. Excepteur sint occaecat cupidatat culpa qui officia deserunt mollit anim id est laborum.</p>
<div class="btn btn-blue" style="left:579px;top:4194px;width:188px;height:44px">Learn More <span class="arr">&#10148;</span></div>

<svg class="abs" style="left:0;top:4270px" width="1200" height="270" viewBox="0 0 1200 270">
  <path d="M0 150 C60 110 200 115 420 118 C700 120 1000 90 1200 0 L1200 270 L0 270 Z" fill="#fff"/>
  <path d="M0 150 C60 110 200 115 420 118 C700 120 1000 90 1200 0 L1200 40 C1020 150 820 225 560 240 C300 255 40 280 0 210 Z" fill="var(--orange)"/>
</svg>

<!-- footer -->
<div class="abs brand" style="left:100px;top:4638px"><span class="mark"></span>Harbor Crest Metrics</div>
<div class="abs socials"><i></i><i></i><i></i><i></i></div>

<div class="abs" style="left:383px;top:4594px">
  <div class="f-head">QUICK LINKS</div><div class="f-bar"></div>
  <ul class="f-list"><li>Home</li><li>Who we are</li><li>What we do</li><li>Mobile app</li><li>Faq</li><li>Customer Service</li></ul>
</div>
<div class="abs" style="left:640px;top:4594px">
  <div class="f-head">INFORMATION</div><div class="f-bar"></div>
  <ul class="f-list"><li>Privacy policy</li><li>Terms &amp; condition</li><li>Support</li><li>Faq</li><li>Blog</li><li>Evevnt</li></ul>
</div>
<div class="abs" style="left:857px;top:4594px">
  <div class="f-head">CONTACT US</div><div class="f-bar"></div>
  <div class="contact-row" style="margin-top:14px"><svg width="10" height="14" viewBox="0 0 10 14"><path d="M5 0a5 5 0 0 1 5 5c0 4-5 9-5 9S0 9 0 5a5 5 0 0 1 5-5z" fill="var(--blue-deep)"/><circle cx="5" cy="5" r="2" fill="#fff"/></svg><span>418 Lantern Quay Rd<br>Suite B2 Bayview, GA 30299</span></div>
  <div class="contact-row" style="margin-top:20px"><svg width="12" height="12" viewBox="0 0 12 12"><path d="M2 0l3 3-1.5 2a7 7 0 0 0 3.5 3.5L9 7l3 3-2 2C5 12 0 7 0 2z" fill="var(--blue-deep)"/></svg><span>Phone : 555.014.2270</span></div>
  <div class="contact-row" style="margin-top:20px"><svg width="13" height="10" viewBox="0 0 13 10"><rect width="13" height="10" rx="1" fill="var(--blue-deep)"/><path d="M0 1l6.5 5L13 1" stroke="#fff" fill="none"/></svg><span>Email : info@harborcrestmetrics.example</span></div>
</div>
<div class="abs divider"></div>
<p class="abs copy">Copyright 2022 Company name | All Rights Reserved</p>

</body>
</html>
```